Topics to Raise With a Clinician tri-fold brochure

We are looking for a 1 page (front and back) 8.5" x 11" tri-fold brochure. Please refer back to our Rack Cards for a similar look and feel to the design. They can be found here: https://otvenrix.org/resources/sunny-garden-steady-mind-rack-card-series/.
This brochure is titled: Topics to Raise With a Clinician on Forgetfulness.

The document is for older readers. Do not put text over graphics and keep it simple and easy to read with high contrast.

We want some very simple design element(s) incorporated that convey Native American communities or heritage. But NO headdress, teepee graphics, owls etc. I have included some images, please use your creative discretion to use which ones look good.

Please remember to include the funding statement - it can be in a very small font 6/7 point: For more information about our project, please visit https://otvenrix.org/mind-care/resources - This rack card is supported by the Bureau for Wellness Tracking and Outreach (BWTO) of the Federal Office of Wellbeing and Family Supports (FWF) as part of a financial assistance award totaling $1,053,119.36 with 100 percent funded by BWTO/FWF. The contents are those of the author(s) and do not necessarily represent the official views of, nor an endorsement, by BWTO/FWF, or the U.S. Government.

Please feel free to choose one of each of the 2 logos that looks best (horizontal or square). We have the OT3 logo and the Cedar Path Learning Hub logo we would like to add. I have added the document and there are images to choose from to use.

I am thinking that the front of the tri-fold should have one of the pictures of a patient and doctor talking. I have included several options. Please use your creative discretion to choose what looks best.

Please let me know if you have any questions, thank you!

```html
<!DOCTYPE html>
<html lang="en">
<head>
<meta charset="utf-8">
<title>Topics to Raise With a Clinician – Tri-fold Brochure</title>
<link rel="stylesheet" href="https://fonts.googleapis.com/css2?family=Montserrat:wght@400;500;600;700;800&display=swap">
<style>
  :root {
    --stage: #545454;
    --paper: #f4f4f3;
    --maroon: #571515;
    --maroon-deep: #430d10;
    --teal: #3c98a1;
    --ink: #3a2626;
    --rule: #3c98a1;
    --photo-warm: #b9b2aa;
    --photo-gray: #6f6f6f;
  }
  * { box-sizing: border-box; margin: 0; padding: 0; }
  html, body { width: 1200px; height: 1001px; overflow: hidden; }
  body {
    background: var(--stage);
    font-family: "Montserrat", Arial, sans-serif;
    color: var(--ink);
    display: flex;
    align-items: center;
    justify-content: center;
    gap: 24px;
  }

  .spread { display: flex; width: 852px; height: 660px; background: var(--paper); }
  .panel { width: 284px; height: 100%; display: flex; flex-direction: column; position: relative; }
  .panel + .panel { border-left: 1px solid #dcdcdc; }

  .panel-head {
    height: 96px; flex: none; background: var(--maroon-deep);
    color: #fff; padding: 20px 20px 0;
    font-weight: 700; font-size: 15px; letter-spacing: .06em; line-height: 1.2;
    text-transform: uppercase;
  }
  .panel-head.blank { background: var(--maroon); }

  .heritage-band {
    height: 14px; flex: none;
    background: linear-gradient(90deg, var(--teal) 0%, var(--maroon) 50%, var(--teal) 100%);
  }

  .panel-body { padding: 18px 18px 0; flex: 1; }

  .ask-list { list-style: none; }
  .ask-item {
    font-weight: 700; font-size: 12.5px; color: var(--maroon-deep);
    padding: 6px 0 4px 14px; border-bottom: 2px solid var(--rule);
    position: relative; line-height: 1.25;
  }
  .ask-item::before {
    content: ""; position: absolute; left: 0; top: 8px;
    width: 8px; height: 8px; background: var(--teal);
  }
  .cause-list { list-style: none; font-size: 11px; font-weight: 500; line-height: 1.35; padding: 6px 0 6px 2px; border-bottom: 2px solid var(--rule); }
  .cause-list li::before, .after-list li::before, .doctor-list li::before { content: "• "; }
  .subhead { font-weight: 700; font-size: 13px; color: var(--maroon-deep); margin-top: 8px; padding-bottom: 3px; border-bottom: 2px solid var(--rule); }
  .after-list { list-style: none; font-size: 10.5px; font-weight: 500; line-height: 1.35; padding-top: 5px; }
  .after-list li { margin-bottom: 3px; }

  .photo-jewelry {
    height: 118px; flex: none;
    background: linear-gradient(135deg, #3b3b3b, var(--photo-gray) 55%, #9a9a9a);
  }

  .section-title {
    font-weight: 700; font-size: 15px; letter-spacing: .04em;
    color: var(--maroon-deep); text-transform: uppercase; line-height: 1.2;
    margin: 16px 0 14px;
  }
  .section-title.centered { text-align: center; }
  .doctor-list { list-style: none; font-size: 11px; font-weight: 500; line-height: 1.3; }
  .doctor-list li { padding: 6px 0 5px; border-bottom: 2px solid var(--rule); }

  .tracking-copy { font-size: 10.5px; font-weight: 500; text-align: center; line-height: 1.35; }

  .tracker { width: 100%; border-collapse: collapse; margin-top: 30px; font-size: 8px; }
  .tracker th { background: var(--maroon); color: #fff; font-weight: 600; padding: 3px 2px; text-align: center; }
  .tracker td { border: 1px solid #555; height: 19px; }

  .tree-art {
    height: 150px; flex: none;
    background: linear-gradient(90deg, #b7b27a 0%, #c88a3c 45%, #b8452a 70%, #f0f0ee 100%);
    position: relative;
  }
  .tree-art::after { content: ""; position: absolute; left: 0; right: 0; bottom: 0; height: 30px; background: #6fa04a; }

  .cover { width: 288px; height: 660px; background: var(--paper); display: flex; flex-direction: column; }
  .cover-brand { padding: 28px 22px 22px; display: flex; gap: 12px; align-items: flex-start; }
  .brand-mark { width: 14px; height: 14px; background: var(--teal); flex: none; margin-top: 4px; }
  .brand-name { font-weight: 700; font-size: 18px; color: var(--maroon); line-height: 1.2; text-transform: uppercase; }
  .cover-photo {
    flex: 1;
    background: linear-gradient(160deg, #e4e1dc 0%, var(--photo-warm) 45%, #7fb3b9 100%);
  }
  .cover-title {
    background: var(--teal); color: #fff;
    font-weight: 700; font-size: 23px; line-height: 1.2;
    padding: 20px 22px;
  }
  .cover-url {
    background: var(--maroon-deep); color: #fff;
    font-weight: 500; font-size: 17px; padding: 22px;
  }
</style>
</head>
<body>

<section class="spread">
  <article class="panel">
    <header class="panel-head">Topics to Raise With a Clinician:</header>
    <div class="heritage-band" role="img" aria-label="Zigzag chevron pattern band inspired by Native American design"></div>
    <div class="panel-body">
      <ul class="ask-list">
        <li class="ask-item">When should I be concerned?</li>
        <li class="ask-item">What kind of testing can be done for memory loss?</li>
        <li class="ask-item">What other things could be causing memory loss?</li>
      </ul>
      <ul class="cause-list">
        <li>Anxiety or depression</li>
        <li>Sleep disorders</li>
        <li>Thyroid problems</li>
        <li>Vitamin deficiencies</li>
        <li>Head injuries</li>
        <li>Dehydration</li>
        <li>Infections (Urinary tract, Respiratory, etc.)</li>
        <li>Medications</li>
      </ul>
      <p class="subhead">What happens after diagnosis?</p>
      <ul class="after-list">
        <li>Are there lifestyle changes that could help?</li>
        <li>What safety measures should be taken? What are the signs of certain activities becoming unsafe?</li>
        <li>What community resources are available?</li>
        <li>How can we prepare for progression?</li>
      </ul>
    </div>
    <div class="photo-jewelry" role="img" aria-label="Black and white photo of traditional silver and turquoise jewelry"></div>
  </article>

  <article class="panel">
    <header class="panel-head blank"></header>
    <div class="heritage-band" role="img" aria-label="Zigzag chevron pattern band inspired by Native American design"></div>
    <div class="panel-body">
      <h2 class="section-title">Questions your doctor may ask you:</h2>
      <ul class="doctor-list">
        <li>When did your symptoms of forgetfulness begin?</li>
        <li>What tasks do you find difficult?</li>
        <li>What specific behaviors related to memory loss are concerning you?</li>
        <li>Have you recently been sick?</li>
        <li>Have you recently been in an accident?</li>
        <li>Have you ever hit your head?</li>
        <li>Do you forget the names of someone close?</li>
        <li>Have you noticed any mood changes?</li>
      </ul>
    </div>
  </article>

  <article class="panel">
    <header class="panel-head blank"></header>
    <div class="heritage-band" role="img" aria-label="Zigzag chevron pattern band inspired by Native American design"></div>
    <div class="panel-body">
      <h2 class="section-title centered">Symptom Tracking:</h2>
      <p class="tracking-copy">By tracking symptoms like forgetfulness, confusion, or difficulty with everyday tasks, individuals and their caregivers can provide accurate information to healthcare providers, leading to better planning and support.<br>A symptom tracker template and examples can be found at</p>
      <table class="tracker">
        <thead><tr><th>Date</th><th>Time</th><th>Location</th><th>Symptoms and Behavior</th></tr></thead>
        <tbody>
          <tr><td></td><td></td><td></td><td></td></tr>
          <tr><td></td><td></td><td></td><td></td></tr>
          <tr><td></td><td></td><td></td><td></td></tr>
          <tr><td></td><td></td><td></td><td></td></tr>
          <tr><td></td><td></td><td></td><td></td></tr>
          <tr><td></td><td></td><td></td><td></td></tr>
        </tbody>
      </table>
    </div>
    <div class="tree-art" role="img" aria-label="Illustration of trees shaped like head profiles losing autumn leaves"></div>
  </article>
</section>

<section class="cover">
  <div class="cover-brand">
    <span class="brand-mark"></span>
    <p class="brand-name">Northern Circle Council on Elder Wellness</p>
  </div>
  <div class="heritage-band" role="img" aria-label="Zigzag chevron pattern band inspired by Native American design"></div>
  <div class="cover-photo" role="img" aria-label="Photo of an older patient talking with a clinician holding a tablet"></div>
  <h1 class="cover-title">Topics to Raise With a Clinician on Forgetfulness</h1>
  <p class="cover-url">otvenrix.org</p>
</section>

</body>
</html>
```